Cover Page for Pixelwall, Workbridge & Dwellora.com

I'm needing a cover page for Pixelwall, Workbridge & Dwellora.com. I already have my logo and some samples of what I'm looking for but open to new ideals. I'm in the real estate business and want something that looks very professional and clean. The area I cover is located in the Lake Norman area of North Carolina so would like to incorporate a lake background along with my logo, headshot and contact information.

```html
<!DOCTYPE html>
<html lang="en">
<head>
<meta charset="utf-8">
<title>Mark Dalton – Broker | Realtor Cover</title>
<link rel="stylesheet" href="https://fonts.googleapis.com/css2?family=Montserrat:wght@400;500;600&display=swap">
<style>
  :root {
    --canvas-bg: #d7dadd;
    --brand-green: #1c8a4c;
    --name-grey: #6a6d71;
    --tag-grey: #55585c;
    --icon-column: #5d6670;
    --white: #ffffff;
  }
  html, body {
    margin: 0;
    padding: 0;
    width: 1200px;
    height: 1200px;
    overflow: hidden;
    background: var(--canvas-bg);
  }
  .canvas {
    position: relative;
    width: 1200px;
    height: 1200px;
  }
  .cover-banner {
    position: absolute;
    left: 50px;
    top: 396px;
    width: 1100px;
    height: 408px;
    display: block;
    box-shadow: 0 6px 20px rgba(0,0,0,0.18);
  }
  .brand-mark { fill: var(--brand-green); }
  .brand-name {
    font-family: "Montserrat", sans-serif;
    font-weight: 500;
    font-size: 31px;
    fill: var(--name-grey);
  }
  .brand-tagline {
    font-family: "Montserrat", sans-serif;
    font-weight: 500;
    font-size: 8.5px;
    letter-spacing: 3.2px;
    fill: var(--tag-grey);
  }
  .contact-line {
    font-family: "Montserrat", sans-serif;
    font-weight: 500;
    font-size: 18.5px;
    fill: var(--white);
  }
  .contact-phone { letter-spacing: 1px; }
  .icon-disc { fill: var(--white); }
  .icon-glyph { fill: none; stroke: var(--icon-column); stroke-width: 1.2; }
</style>
</head>
<body>
<div class="canvas">
  <svg class="cover-banner" viewBox="0 0 851 316" xmlns="http://www.w3.org/2000/svg">
    <defs>
      <linearGradient id="sunset-lake" x1="0" y1="0" x2="0" y2="1">
        <stop offset="0" stop-color="#5a7690"/>
        <stop offset="0.38" stop-color="#e39a55"/>
        <stop offset="0.52" stop-color="#f2c47c"/>
        <stop offset="0.62" stop-color="#3e6b74"/>
        <stop offset="0.85" stop-color="#233f4c"/>
        <stop offset="1" stop-color="#17262e"/>
      </linearGradient>
      <linearGradient id="light-wedge" x1="0" y1="0" x2="0" y2="1">
        <stop offset="0" stop-color="#ffffff" stop-opacity="0.97"/>
        <stop offset="0.5" stop-color="#fdf6ea" stop-opacity="0.9"/>
        <stop offset="0.72" stop-color="#ffffff" stop-opacity="0"/>
      </linearGradient>
      <linearGradient id="headshot-tone" x1="0" y1="0" x2="0" y2="1">
        <stop offset="0" stop-color="#7a6f68" stop-opacity="0.55"/>
        <stop offset="0.3" stop-color="#4a5f82" stop-opacity="0.85"/>
        <stop offset="1" stop-color="#2b3f62"/>
      </linearGradient>
      <linearGradient id="contact-band" x1="0" y1="0" x2="1" y2="0">
        <stop offset="0" stop-color="#1c8a4c" stop-opacity="0"/>
        <stop offset="0.35" stop-color="#1c8a4c" stop-opacity="0.85"/>
        <stop offset="1" stop-color="#1c8a4c" stop-opacity="0.95"/>
      </linearGradient>
    </defs>

    <rect class="scene-photo" x="0" y="0" width="851" height="316" fill="url(#sunset-lake)"
          role="img" aria-label="Sunset over a lake marina with docks, boats and waterfront homes"/>
    <polygon class="light-wedge" points="440,0 851,0 851,316 330,316" fill="url(#light-wedge)"/>

    <rect class="headshot-photo" x="60" y="0" width="320" height="316"
          fill="url(#headshot-tone)" role="img" aria-label="Headshot of the broker in a blue plaid suit"/>

    <g class="brand-lockup">
      <rect class="brand-mark" x="583" y="34" width="56" height="56"/>
      <text class="brand-name" x="611" y="131" text-anchor="middle">MARK DALTON</text>
      <text class="brand-tagline" x="611" y="146" text-anchor="middle">BROKER | REALTOR</text>
    </g>

    <g class="contact-panel">
      <rect x="415" y="182" width="407" height="91" fill="url(#contact-band)"/>
      <rect x="822" y="182" width="29" height="91" fill="var(--icon-column)"/>

      <text class="contact-line contact-phone" x="812" y="209" text-anchor="end">555-014-2276</text>
      <text class="contact-line" x="812" y="236" text-anchor="end">www.markd.shorelinehomes.com</text>
      <text class="contact-line" x="812" y="262" text-anchor="end">markd@shorelinehomes.com</text>

      <g class="icon-phone">
        <circle class="icon-disc" cx="836" cy="203" r="8.5"/>
        <path class="icon-glyph" d="M832.5,199 q-1,3 2,6 q3,3 6,2 l-1.5,-2 l-2,0.5 q-2,-1 -3,-3 l0.5,-2 z"/>
      </g>
      <g class="icon-web">
        <circle class="icon-disc" cx="836" cy="230.5" r="8.5"/>
        <circle class="icon-glyph" cx="836" cy="230.5" r="5"/>
        <ellipse class="icon-glyph" cx="836" cy="230.5" rx="2.2" ry="5"/>
        <line class="icon-glyph" x1="831" y1="230.5" x2="841" y2="230.5"/>
      </g>
      <g class="icon-mail">
        <circle class="icon-disc" cx="836" cy="257" r="8.5"/>
        <rect class="icon-glyph" x="831.5" y="254" width="9" height="6"/>
        <polyline class="icon-glyph" points="831.5,254 836,257.5 840.5,254"/>
      </g>
    </g>
  </svg>
</div>
</body>
</html>
```